New Webpage for High Class Expert Witness Services Company

We are looking for a minimalist design for a webpage that just has our logo and an entry form offer to connect with one of our Liaisons.
The entry form should just ask for Name, Email, Contact Info and Description of Project.

Company Name is: The Marlow Crest Advisory Services

Number of Pages Required

1 page

```html
<!DOCTYPE html>
<html lang="en">
<head>
<meta charset="utf-8">
<title>The Marlow Crest Advisory Services – Connect with a Defense Liaison</title>
<link href="https://fonts.googleapis.com/css2?family=Montserrat:wght@500;600&family=Roboto:wght@400;500;700&display=swap" rel="stylesheet">
<style>
:root{
  --ink:#121212;
  --white:#ffffff;
  --panel:#f4f3fc;
  --field-border:#dcdce4;
  --placeholder:#9a9a9a;
  --footer-text:#9d9d9d;
  --hero-a:#5f8fa6;
  --hero-b:#4c7e97;
  --hero-c:#3d6f88;
}
*{box-sizing:border-box;margin:0;padding:0}
html,body{width:1200px;height:1061px;overflow:hidden;background:var(--white);font-family:'Roboto',sans-serif;color:var(--ink)}
.site-header{height:83px;background:var(--ink);display:flex;align-items:center;justify-content:center}
.brand{display:flex;align-items:center;gap:10px;color:var(--white);font-family:'Montserrat',sans-serif;font-weight:500;letter-spacing:.04em;white-space:nowrap}
.brand-mark{width:14px;height:14px;background:var(--white)}
.site-header .brand{font-size:20px}
.hero{position:relative;height:209px;display:flex;flex-direction:column;align-items:center;justify-content:center;color:var(--white);text-align:center}
.hero-photo{position:absolute;inset:0;background:linear-gradient(120deg,var(--hero-a),var(--hero-b) 55%,var(--hero-c))}
.hero-title{position:relative;font-family:'Montserrat',sans-serif;font-weight:600;font-size:37.5px;text-shadow:0 2px 4px rgba(0,0,0,.25);margin-top:-10px}
.hero-sub{position:relative;font-weight:500;font-size:19px;margin-top:4px;text-shadow:0 2px 4px rgba(0,0,0,.3)}
.contact-card{position:absolute;left:152px;top:352px;width:896px;height:586px;display:flex;border-radius:10px;overflow:hidden}
.card-aside{width:279px;background:var(--ink);color:var(--white);position:relative;text-align:center}
.card-aside .brand{position:absolute;left:26px;top:38px;font-size:12px;gap:7px}
.card-aside .brand-mark{width:9px;height:9px}
.aside-title{position:absolute;left:0;right:0;top:229px;font-family:'Montserrat',sans-serif;font-weight:500;font-size:19.5px;line-height:1.25;white-space:nowrap}
.aside-text{position:absolute;left:0;right:0;top:294px;font-weight:500;font-size:13.6px;line-height:1.2;white-space:nowrap}
.card-form{flex:1;background:var(--panel);padding:57px 29px 0 29px;position:relative}
.field-label{display:block;font-weight:500;font-size:13.6px;height:20px;line-height:20px;margin-bottom:10px}
.field{display:block;width:558px;height:44px;border:1px solid var(--field-border);border-radius:5px;background:var(--white);padding:0 15px;font:400 13.6px 'Roboto',sans-serif;color:var(--ink);margin-bottom:13px}
.field::placeholder{color:var(--placeholder)}
textarea.field{height:117px;padding-top:13px;resize:none}
.submit{position:absolute;left:246px;top:503px;width:121px;height:41px;border:0;border-radius:5px;background:var(--ink);color:var(--white);font:700 16px 'Roboto',sans-serif;letter-spacing:.03em}
.site-footer{position:absolute;left:0;top:1012px;width:1200px;height:49px;background:var(--ink);color:var(--footer-text);font-size:12.5px;display:flex;align-items:center;justify-content:space-between;padding:0 63px 0 62px}
.footer-links span{margin:0 12px}
</style>
</head>
<body>
<header class="site-header">
  <div class="brand"><span class="brand-mark"></span>The Marlow Crest Advisory Services</div>
</header>
<section class="hero">
  <div class="hero-photo" role="img" aria-label="Medical supplies on a blue surface: ribbon, glucose meter, syringes and pills"></div>
  <h1 class="hero-title">Connect with a Defense Liaison</h1>
  <p class="hero-sub">Tell us about your needs. Our team will reach out promptly and confidentially.</p>
</section>
<main class="contact-card">
  <aside class="card-aside">
    <div class="brand"><span class="brand-mark"></span>The Marlow Crest Advisory Services</div>
    <h2 class="aside-title">Lorem Ipsum is simply<br>dummy text of the</h2>
    <p class="aside-text">Lorem Ipsum has been the industry's<br>standard dummy text ever since the<br>1500s, when an unknown printer</p>
  </aside>
  <form class="card-form">
    <label class="field-label" for="name">Full Name</label>
    <input class="field" id="name" type="text" placeholder="Full Name">
    <label class="field-label" for="email">Email Address</label>
    <input class="field" id="email" type="email" placeholder="Email Address">
    <label class="field-label" for="contact">Contact Info (Phone/WhatsApp)</label>
    <input class="field" id="contact" type="text" placeholder="Contact Info (Phone/WhatsApp)">
    <label class="field-label" for="project">Project Description</label>
    <textarea class="field" id="project" placeholder="Project Description"></textarea>
    <button class="submit" type="submit">SUBMIT</button>
  </form>
</main>
<footer class="site-footer">
  <p>Copyright 2026 © The Marlow Crest Advisory Services, All Rights Reserved.</p>
  <p class="footer-links">Confidential<span>|</span>Secure<span>|</span>Trusted</p>
</footer>
</body>
</html>
```